Bref créative
Business cards for comic book store
Use same font as used in my logo
Bartholomew Finch
Owner
4862 North Pellam Avenue
Marrowfield, OR 97381
bart@qtrzinepress.com
www.QTRZinePress.com
ORACLE OF EMBERFALL
DRAVINOK
TITANPEGS
ZE-RA-KU!
COMIC BOOKS
BOARD GAMES
COLLECTIBLES
STATUES
"ASK ME HOW TO SAVE 10% ON YOUR COMIC PURCHASES"
Ai file for Logo

```html
<!DOCTYPE html>
<html lang="en">
<head>
<meta charset="utf-8">
<title>QTR Zine Press – Business Cards</title>
<link href="https://fonts.googleapis.com/css2?family=Bangers&family=Open+Sans:wght@400;600;700&display=swap" rel="stylesheet">
<style>
  :root {
    --stage: #2b2b2d;
    --card-black: #0d0d0d;
    --hero-red: #e0262b;
    --deep-red: #a3141a;
    --hero-blue: #1f6fc2;
    --cloud-white: #ffffff;
    --text-light: #e8e8e8;
  }
  html, body {
    margin: 0;
    width: 1200px;
    height: 857px;
    overflow: hidden;
    background: var(--stage);
    font-family: "Open Sans", Arial, sans-serif;
  }
  .stage {
    position: relative;
    width: 1200px;
    height: 857px;
  }
  .card {
    position: absolute;
    top: 148px;
    width: 330px;
    height: 560px;
    border-radius: 18px;
    overflow: hidden;
    background: var(--card-black);
    box-shadow: 0 12px 30px rgba(0,0,0,0.5);
  }
  .card-back { left: 230px; }
  .card-front { left: 640px; }
  .card-art {
    position: absolute;
    inset: 0;
  }
  /* back */
  .offer-list {
    position: absolute;
    top: 150px;
    left: 0;
    width: 330px;
    text-align: center;
    font-family: "Bangers", "Open Sans", sans-serif;
    letter-spacing: 0.5px;
  }
  .offer-list ul {
    list-style: none;
    margin: 0;
    padding: 0;
    color: var(--hero-blue);
    font-size: 19px;
    line-height: 1.22;
  }
  .offer-quote {
    margin: 12px auto 0;
    width: 220px;
    color: var(--hero-red);
    font-size: 18px;
    line-height: 1.2;
  }
  /* front */
  .mascot-art {
    position: absolute;
    top: 28px;
    left: 60px;
    width: 210px;
    height: 140px;
    border-radius: 14px;
    background: linear-gradient(135deg, #3d86d6 0%, #f2f2f2 50%, #d8262c 100%);
  }
  .brand-name {
    position: absolute;
    top: 172px;
    left: 0;
    width: 330px;
    text-align: center;
    font-family: "Bangers", "Open Sans", sans-serif;
    font-size: 30px;
    color: var(--hero-red);
    letter-spacing: 1px;
  }
  .contact {
    position: absolute;
    top: 352px;
    left: 0;
    width: 330px;
    text-align: center;
    color: var(--text-light);
    font-size: 12px;
    line-height: 1.45;
  }
  .person-name {
    margin: 0;
    color: var(--hero-red);
    font-size: 21px;
    font-weight: 600;
  }
  .person-role {
    margin: 0 0 16px;
    font-size: 12px;
  }
  .address { margin: 0 0 4px; }
  .contact-line {
    display: flex;
    justify-content: center;
    align-items: center;
    gap: 6px;
    margin: 0;
  }
  .contact-line svg { width: 10px; height: 10px; fill: var(--hero-red); }
</style>
</head>
<body>
<main class="stage">

  <section class="card card-back">
    <svg class="card-art" viewBox="0 0 330 560" aria-hidden="true">
      <defs>
        <radialGradient id="burstRed" cx="50%" cy="50%" r="60%">
          <stop offset="0" stop-color="#ff4a4f"/>
          <stop offset="1" stop-color="#a3141a"/>
        </radialGradient>
      </defs>
      <rect width="330" height="560" fill="#0d0d0d"/>
      <path d="M0 70 Q60 40 110 70 Q165 30 220 70 Q280 40 330 70 V490 Q270 520 220 490 Q165 530 110 490 Q60 520 0 490 Z" fill="url(#burstRed)"/>
      <path d="M0 84 Q60 56 110 84 Q165 46 220 84 Q280 56 330 84 V476 Q270 504 220 476 Q165 514 110 476 Q60 504 0 476 Z" fill="none" stroke="#1f6fc2" stroke-width="6"/>
      <path d="M40 140 Q30 110 70 110 Q90 80 130 98 Q165 70 200 98 Q245 82 262 112 Q300 115 292 150 Q318 190 296 230 Q318 280 294 320 Q312 370 280 400 Q278 440 236 440 Q205 468 165 448 Q125 468 95 442 Q52 446 50 405 Q16 380 34 330 Q12 280 34 240 Q14 190 40 140 Z" fill="#ffffff"/>
    </svg>
    <div class="offer-list">
      <ul>
        <li>ORACLE OF EMBERFALL</li>
        <li>DRAVINOK</li>
        <li>TITANPEGS</li>
        <li>ZE-RA-KU!</li>
        <li>COMIC BOOKS</li>
        <li>BOARD GAMES</li>
        <li>COLLECTIBLES</li>
        <li>STATUES</li>
      </ul>
      <p class="offer-quote">"ASK ME HOW TO SAVE 10% ON YOUR COMIC PURCHASES"</p>
    </div>
  </section>

  <section class="card card-front">
    <svg class="card-art" viewBox="0 0 330 560" aria-hidden="true">
      <defs>
        <radialGradient id="bandRed" cx="50%" cy="0%" r="90%">
          <stop offset="0" stop-color="#ff4a4f"/>
          <stop offset="1" stop-color="#a3141a"/>
        </radialGradient>
      </defs>
      <rect width="330" height="560" fill="#0d0d0d"/>
      <path d="M0 0 H330 V300 Q280 325 220 300 Q165 335 110 300 Q55 325 0 300 Z" fill="url(#bandRed)"/>
      <path d="M0 0 H330 V230 Q280 250 220 228 Q165 262 110 228 Q55 250 0 230 Z" fill="#1f6fc2"/>
      <path d="M0 0 H330 V218 Q280 238 220 216 Q165 250 110 216 Q55 238 0 218 Z" fill="#ffffff"/>
    </svg>
    <div class="mascot-art" role="img" aria-label="Illustration of a caped hero and a winged villain mascot pair"></div>
    <div class="brand-name">QTR Zine Press</div>
    <div class="contact">
      <p class="person-name">Bartholomew Finch</p>
      <p class="person-role">Owner</p>
      <p class="address">4862 North Pellam Avenue<br>Marrowfield, OR 97381</p>
      <p class="contact-line"><svg viewBox="0 0 10 10"><circle cx="5" cy="5" r="5"/></svg>(541) 555-0142</p>
      <p class="contact-line"><svg viewBox="0 0 10 10"><circle cx="5" cy="5" r="5"/></svg>bart@qtrzinepress.com</p>
      <p class="contact-line"><svg viewBox="0 0 10 10"><circle cx="5" cy="5" r="5"/></svg>www.QTRZinePress.com</p>
    </div>
  </section>

</main>
</body>
</html>
```